Natural Skincare Product Labels Design

We are looking for a designer to create elegant but quirky, functional product labels for our natural skincare range.
The labels must reflect our brand’s values of simplicity, luxury, and the natural, handmade essence of our products.
https://www.instagram.com/tolvarenskincare
1. Key Details
Packaging Dimensions
Container Types: Transparent jars.
Sizes for Body Products:
Diameter: 64mm–68mm.
Heights: 80mm, 88mm, and 97mm (lid height: 15mm).
Sizes for Face Creams:
Diameter: 60mm.
Height: 50mm (lid height: 15mm).
Label Fit: For body products, ideally one label size to fit all jar sizes.
For the smaller face cream jars, a separate, tailored label is required.
2. Label Placement
Options include a wrapped-around label or a combination of wrapped-around and top-of-jar elements.
Transparent jars mean the label must leave space for the product to be visible (e.g., partial wrap or cutout areas).
3. Content Requirements
Product Name: Prominently displayed.
Ingredient List: Dedicated space required.
Disclaimer/Usage Instructions: Include space for this information.
4. Design Goals
Look & Feel: Simple, upmarket, and natural, with a handmade essence.
Logo Usage: Our logo is finalized and available in gold, black, and white variants. Use Josefin Bold font for the logo if adjustments are required.
Color Palette: Neutral tones (e.g., whites, blacks, golds) are preferred, with flexibility for subtle pops of color tied to each product’s main ingredient.
5. Imagery
Open to including images and colours (e.g., botanical illustrations) that highlight the main ingredient (e.g., coffee beans, turmeric root, or honeycomb). Also open to labels having a prominent colour to tie it in to the main ingredient.
Alternatively, no images can also work for a clean design.
6. Current Design Context
Our temporary design features gold leaf on top and a simple handmade side label. We’re seeking to elevate this to a more polished, cohesive design.
7. Product Line
- Body Products (Larger Jars)
Mivo Body Butter
Key Ingredients: Guarana & Cupuaçu butter (inspired by Brazil).
Note: “Mivo” is slang for “bum.”
Manuka Honey Body Butter
Key Ingredients: Manuka honey (from New Zealand) & Cupuaçu butter.
Coffee Body Scrub
Key Ingredients: Coffee and Demerara sugar.
Whipped Body Soap - Turmeric
Key Ingredients: Turmeric and Bentonite clay.
Whipped Body Soap - Banana
- Face Products (Smaller Jars)
Face Cream
Key Ingredients: Carrot Oil and Raspberry Oil.
Features natural UV protection.
Good Night Cream
Key Ingredients: Enriched with Magnesium.
Promotes relaxation and restful sleep.
8. Submission Guidelines
Flexibility: Design should allow for consistent branding across all products while accommodating the varying jar sizes and ingredient focus.
Material Considerations: Labels should complement the transparent jars and allow the product inside to remain partially visible.
Print Elements: Incorporating gold accents is a plus but should not overpower the design.
We’re excited to see your vision for a label that celebrates the natural beauty and high quality of our skincare range. Please include mockups to showcase the design in use, particularly on transparent jars of varying sizes.
women 20-50 years of age

```html
<!DOCTYPE html>
<html lang="en">
<head>
<meta charset="utf-8">
<title>Tolvaren Body Butter Labels</title>
<link rel="stylesheet" href="https://fonts.googleapis.com/css2?family=Montserrat:wght@400;500;600&display=swap">
<style>
  :root {
    --canvas: #ffffff;
    --label: #f7f7f7;
    --label-edge: #dedede;
    --ink: #1b1b1b;
    --gold: #f1ac22;
    --sketch-light: #fafafa;
    --sketch-dark: #d9d9d9;
    --frame: #222222;
  }
  * { margin: 0; padding: 0; box-sizing: border-box; }
  html, body { width: 1200px; height: 1200px; overflow: hidden; background: var(--canvas); }
  body { position: relative; font-family: "Montserrat", Arial, sans-serif; color: var(--ink); }

  /* Front panels */
  .front-label {
    position: absolute; top: 180px; width: 336px; height: 270px;
    background: linear-gradient(90deg, #ececec 0%, var(--label) 30%, #ffffff 55%, #efefef 100%);
    border-top: 1px solid var(--label-edge); border-bottom: 1px solid var(--label-edge);
    overflow: hidden; text-align: center;
  }
  .front-label--manuka-gold { left: 62px; }
  .front-label--mivo { left: 428px; }
  .front-label--manuka-ink { left: 786px; }

  .botanical {
    position: absolute;
    background: radial-gradient(ellipse at 50% 50%, var(--sketch-dark) 0%, #e6e6e6 40%, rgba(240,240,240,0) 72%);
  }
  .front-label .botanical { left: 200px; top: 70px; width: 160px; height: 210px; }

  .brand { position: absolute; left: 0; right: 0; display: flex; justify-content: center; align-items: center; gap: 6px;
    color: var(--gold); font-weight: 500; letter-spacing: 0.22em; }
  .brand-dot { border-radius: 50%; background: var(--gold); }
  .front-label .brand { top: 56px; font-size: 11px; }
  .front-label .brand-dot { width: 5px; height: 5px; }

  .product-name { position: absolute; left: 0; right: 0; font-weight: 500; letter-spacing: 0.12em; line-height: 0.95; }
  .product-name small { display: block; letter-spacing: 0.2em; }
  .front-label .product-name { top: 96px; font-size: 15px; color: var(--gold); }
  .front-label .product-name small { font-size: 12.5px; }
  .front-label--manuka-ink .product-name { color: var(--ink); }
  .front-label--mivo .product-name { top: 100px; font-size: 24px; font-weight: 600; }

  .product-type { position: absolute; left: 0; right: 0; font-weight: 500; letter-spacing: 0.08em; line-height: 0.95; }
  .front-label .product-type { top: 148px; font-size: 26px; }
  .gold-rule { position: absolute; left: 50%; height: 2px; background: var(--gold); }
  .front-label .gold-rule { top: 202px; width: 28px; margin-left: -14px; }
  .key-ingredients { position: absolute; left: 0; right: 0; font-weight: 500; }
  .front-label .key-ingredients { top: 218px; font-size: 7.5px; line-height: 1.55; }

  /* Full wrap label */
  .wrap-label {
    position: absolute; left: 231px; top: 644px; width: 801px; height: 354px;
    border: 1px solid var(--frame); background: #fff; overflow: hidden;
  }
  .wrap-label .botanical { left: 440px; top: 95px; width: 175px; height: 259px; }
  .wrap-label .brand { top: 68px; font-size: 14px; }
  .wrap-label .brand-dot { width: 6px; height: 6px; }
  .wrap-label .product-name { top: 118px; font-size: 20px; color: var(--gold); text-align: center; }
  .wrap-label .product-name small { font-size: 17px; }
  .wrap-label .product-type { top: 180px; font-size: 32px; text-align: center; }
  .wrap-label .gold-rule { top: 243px; width: 30px; margin-left: -15px; }
  .wrap-label .key-ingredients { top: 263px; font-size: 8.5px; line-height: 1.6; text-align: center; }

  .panel-heading { font-size: 16.5px; font-weight: 600; letter-spacing: 0.02em; margin-bottom: 8px; }
  .panel-copy { font-size: 9.5px; font-weight: 500; line-height: 1.27; text-transform: uppercase; }
  .ingredients { position: absolute; left: 38px; top: 78px; width: 190px; }
  .directions { position: absolute; right: 30px; top: 78px; width: 150px; text-align: right; }
  .directions .panel-heading { margin-bottom: 12px; }
  .storage { position: absolute; left: 38px; top: 278px; }
  .net-weight { position: absolute; left: 38px; top: 315px; font-size: 12px; font-weight: 500; }
  .warnings { position: absolute; right: 29px; top: 277px; width: 150px; text-align: right; }
</style>
</head>
<body>

  <section class="front-label front-label--manuka-gold">
    <div class="botanical" role="img" aria-label="Grey pencil botanical sketch of manuka blossoms"></div>
    <div class="brand"><span class="brand-dot"></span>TOLVAREN</div>
    <h2 class="product-name">MANUKA<small>HONEY</small></h2>
    <h1 class="product-type">BODY<br>BUTTER</h1>
    <div class="gold-rule"></div>
    <p class="key-ingredients">Manuka honey (from New Zealand)<br>&amp; Cupuaçu butter.</p>
  </section>

  <section class="front-label front-label--mivo">
    <div class="botanical" role="img" aria-label="Grey pencil botanical sketch of guarana fruit"></div>
    <div class="brand"><span class="brand-dot"></span>TOLVAREN</div>
    <h2 class="product-name">MIVO</h2>
    <h1 class="product-type">BODY<br>BUTTER</h1>
    <div class="gold-rule"></div>
    <p class="key-ingredients">Guarana &amp; Cupuaçu butter</p>
  </section>

  <section class="front-label front-label--manuka-ink">
    <div class="botanical" role="img" aria-label="Grey pencil botanical sketch of manuka blossoms"></div>
    <div class="brand"><span class="brand-dot"></span>TOLVAREN</div>
    <h2 class="product-name">MANUKA<small>HONEY</small></h2>
    <h1 class="product-type">BODY<br>BUTTER</h1>
    <div class="gold-rule"></div>
    <p class="key-ingredients">Manuka honey (from New Zealand)<br>&amp; Cupuaçu butter.</p>
  </section>

  <section class="wrap-label">
    <div class="botanical" role="img" aria-label="Grey pencil botanical sketch of manuka blossoms and leaves"></div>

    <div class="ingredients">
      <h3 class="panel-heading">INGREDIENTS</h3>
      <p class="panel-copy">Lorem ipsum dolor sit amet, consectetuer adipiscing elit, sed diam nonummy nibh euismod tincidunt ut laoreet dolore</p>
    </div>
    <p class="panel-copy storage">Store in a cold dry place,<br>away from direct sunlight</p>
    <p class="net-weight">NET WT. 8OZ | 240 G</p>

    <div class="brand"><span class="brand-dot"></span>TOLVAREN</div>
    <h2 class="product-name">MANUKA<small>HONEY</small></h2>
    <h1 class="product-type">BODY<br>BUTTER</h1>
    <div class="gold-rule"></div>
    <p class="key-ingredients">Manuka honey (from New Zealand)<br>&amp; Cupuaçu butter.</p>

    <div class="directions">
      <h3 class="panel-heading">DIRECTIONS</h3>
      <p class="panel-copy">Lorem ipsum dolor sit amet, consec-tetuer adipiscing elit, sed diam nonummy nibh euismod tincid-unt ut laoreet dolore magna</p>
    </div>
    <p class="panel-copy warnings">Lorem ipsum dolor sit amet, consec-tetuer adipiscing elit, sed diam nonummy nibh euismod tincid-</p>
  </section>

</body>
</html>
```